Water filter company needs packaging designs

Clervia is a new company that makes eco-friendly water filter for consumers . we currently need designs for our 13 stage water filter, alkaline filter and their respective replacement cartridges.we would like to see a final design that reflect Eco-friendliness, safeness, uniqueness, healthiness,cleanliness and life.

https://www.stashcove.com/s/k8r2mqw7tnvlax3/image%201.png
https://www.stashcove.com/s/h3w91pzr6ck4dme/image%204%20%281%29.png
https://www.stashcove.com/s/7vtmx4kqe2nrwyb/image%206%20png.png"

some of the images i attached for use are also available a this dropbox link

https://www.stashcove.com/sh/pqe4ktyvrm8lown/KXafRe_T3?n=58203714

sorry everyone i forgot to add the dimensions.
13 stage and alkaline filter have the same dimensions of

Size { W x H x L }: 4.5 x 12 x 5.375 INCHES
their cartidges have the same dimensions of
Size { W x H x L }: 3.125 x 10 x 3.125 INCHES

include "Made in U.S.A" on all packaging boxes.

I just found out that the people at artfolio screwed up the order of the files I sent in for upload.Here is an update on that . For 13 stage water filter and it's replacement cartridge box, use the files with following names only  and any corresponding description - 13 stage cartridge, image 1, image 4,image 2, image 6 ,logo,front panel image,13 stage water filter and 13 stage water filter replacement cartridge.For alkaline filter and it;s replacement filter, use files with the following names only and any corresponding description-  8 stage cartridge,active girl,front panel image,glass girl, jumping girl,yoga girl,clervia alkaline water filter, clervia alkaline water filter replacement cartridge,logo

uploaded water splash image for background.You can revise your work with that if you wish to.Thanks

consumers for home use

It Company

• must use all photos attached with appropriate descriptions
must be in retail packaging

```html
<!DOCTYPE html>
<html lang="en">
<head>
<meta charset="utf-8">
<title>Clervia 13-Stage Water Filter Box Front</title>
<link rel="stylesheet" href="https://fonts.googleapis.com/css2?family=Kalam:wght@700&family=Kaushan+Script&family=Lilita+One&family=Roboto+Condensed:wght@400&family=Nunito:wght@800&display=swap">
<style>
  :root {
    --sky-top: #d6e8f4;
    --sky-mid: #a8cbe6;
    --horizon: #c9dbe8;
    --sea-light: #2f78b6;
    --sea-deep: #0c3f78;
    --eco-green: #1f6b3c;
    --brand-blue: #1c78c8;
    --tagline: #6aa0cf;
    --title-teal: #17a09e;
    --title-edge: #ffffff;
    --window-edge: #3a4148;
    --window-fill: #ffffff;
    --script-white: #ffffff;
    --flag-red: #c8303a;
    --flag-blue: #2a3f8f;
    --glow: #f6f8fa;
  }
  * { margin: 0; padding: 0; box-sizing: border-box; }
  html, body { width: 1200px; height: 3200px; overflow: hidden; background: #ffffff; }
  .box-front {
    position: relative;
    width: 1200px;
    height: 3200px;
    overflow: hidden;
  }
  .backdrop {
    position: absolute; inset: 0;
    background: linear-gradient(180deg,
      var(--sky-top) 0%, var(--sky-mid) 38%, var(--horizon) 50%,
      var(--sea-light) 53%, var(--sea-deep) 100%);
  }
  .eco-badge {
    position: absolute;
    left: 70px; top: 40px;
    color: var(--eco-green);
    font-family: "Kalam", cursive;
    font-weight: 700;
    transform: rotate(-12deg);
    transform-origin: left top;
    line-height: 0.9;
  }
  .eco-badge .eco-word { display: block; font-size: 110px; padding-left: 190px; }
  .eco-badge .friendly-word { display: block; font-size: 140px; }
  .brand {
    position: absolute;
    left: 0; right: 0; top: 290px;
    text-align: center;
  }
  .brand-mark {
    width: 250px; height: 250px; margin: 0 auto;
    border-radius: 50%;
    background: var(--brand-blue);
  }
  .brand-name {
    margin-top: 130px;
    font-family: "Nunito", sans-serif;
    font-weight: 800;
    font-size: 58px;
    color: var(--brand-blue);
    line-height: 1;
  }
  .brand-tagline {
    font-family: "Nunito", sans-serif;
    font-weight: 800;
    font-size: 28px;
    color: var(--tagline);
    line-height: 1.2;
  }
  .product-title {
    position: absolute;
    left: 0; right: 0; top: 925px;
    text-align: center;
    font-family: "Lilita One", sans-serif;
    font-size: 112px;
    color: var(--title-teal);
    -webkit-text-stroke: 10px var(--title-edge);
    paint-order: stroke fill;
    text-shadow: 6px 8px 10px rgba(0,0,0,0.35);
    letter-spacing: 1px;
  }
  .product-window {
    position: absolute;
    left: 389px; top: 1140px;
    width: 489px; height: 941px;
    border-radius: 95px;
    background: var(--window-fill);
    border: 14px solid var(--window-edge);
    box-shadow: 0 0 0 14px #ffffff, 0 18px 40px rgba(0,0,0,0.45);
  }
  .model-photo {
    position: absolute;
    left: 300px; top: 2120px;
    width: 900px; height: 1080px;
    background: radial-gradient(ellipse 55% 50% at 55% 55%,
      var(--glow) 0%, rgba(240,236,230,0.85) 45%, rgba(240,236,230,0) 75%);
  }
  .quality-script {
    position: absolute;
    left: 80px; top: 2130px;
    color: var(--script-white);
    font-family: "Kaushan Script", cursive;
    font-size: 140px;
    line-height: 0.95;
    transform: rotate(-14deg);
    transform-origin: left top;
    text-shadow: 0 4px 10px rgba(0,0,0,0.25);
  }
  .quality-script .second-line { display: block; padding-left: 140px; }
  .origin-flag {
    position: absolute;
    left: 108px; top: 2693px;
    width: 244px; height: 244px;
    border-radius: 50%;
    background: linear-gradient(135deg, var(--flag-blue) 0%, var(--flag-blue) 40%, var(--flag-red) 40%, #ffffff 70%, var(--flag-red) 100%);
    box-shadow: 0 6px 14px rgba(0,0,0,0.35);
  }
  .origin-label {
    position: absolute;
    left: 100px; top: 2950px;
    font-family: "Roboto Condensed", sans-serif;
    color: #ffffff;
    line-height: 1;
  }
  .origin-label .small { font-size: 50px; }
  .origin-label .large { font-size: 76px; }
</style>
</head>
<body>
<main class="box-front">
  <div class="backdrop" role="img" aria-label="Photo of a calm blue sea under a pale sky with distant hills on the horizon"></div>

  <div class="eco-badge">
    <span class="eco-word">Eco</span>
    <span class="friendly-word">Friendly</span>
  </div>

  <div class="brand">
    <div class="brand-mark"></div>
    <div class="brand-name">Clervia</div>
    <div class="brand-tagline">Let's treasure our future</div>
  </div>

  <h1 class="product-title">13-Stage Water Filter</h1>

  <div class="product-window"></div>

  <div class="model-photo" role="img" aria-label="Photo of a woman in white clothing sitting in a yoga pose on a rock by the sea"></div>

  <div class="quality-script">
    <span>Purest</span>
    <span class="second-line">Quality</span>
  </div>

  <div class="origin-flag" role="img" aria-label="Round United States flag emblem"></div>
  <div class="origin-label"><span class="small">Made in </span><span class="large">USA</span></div>
</main>
</body>
</html>
```